Flyer Needed to Advertise New Online Reading Programs

ABOUT THE TRUST OF READING DEVELOPMENT
The Trust teaches summer reading skills programs for elementary school students, in programs offered through partnerships with universities, colleges and municipalities nationwide. The goal of each program is to build reading skills, and to foster a lifetime love of books and reading.

AIMS & TARGET MARKET
The Trust has developed a new format of its’ online reading program for elementary students, which includes live small-group video classes taught by a professional reading teacher. The Trust seeks a new graphic design for a flyer to advertise the new online reading program. The flyer will be sent to elementary schools, passed out by teachers, and then taken home by students to show parents; therefore, the primary audience for the flyer will be teachers and parents of elementary school students.

Live classes for children are completely new in online education, unlike anything else in the marketplace, and parents and teachers therefore have no experience with them. The successful design will include illustrations or photographs that allow visitors to immediately grasp/understand the new video class format, without relying heavily on a written description. Additionally, the successful flyer concept will make the program, and the video classes in particular, feel fun and appealing to kids and parents.

Below is additional information about the new live small-group video class format, which meets weekly for 6 weeks:
o During video classes, students participate from home.
o During discussions, the student’s computer (or tablet) screen is filled with live video frames of the teacher and the other students. The video frame for the teacher is larger, and the other students appear in smaller frames.
o During other video class instruction, the teacher uses a presentation screen to display pages of a book or a “whiteboard” used for instructional activities.

Notes: The flyer design could include an illustrated or photo screenshot of a video class, with children looking engaged and a teacher leading them in discussion (stock photos are okay to use in flyer design). We have included a screen shot of one of these classes for reference, but do not feel constrained to represent this screen realistically (as shown here). Layout, look and feel can be changed. Alternatively, you may choose to use a graphic other than a screenshot to bring across the concept of the video classes.

COPY AND SPECIFICATIONS
The flyer design will be one-sided and the dimensions are 8.5” x 11” in either portrait or landscape orientation. We will consider designs in color or black and white. Since we brand our flyers with logos of the universities we partner with throughout the nation, we’ll need to include a partner logo in the design. Exact copy will be provided, but layout is flexible. Screenshots from our sample classes are included to show screen layout. Stock photos are okay to use in flyer designs.

Reason: We'd like to make edits to existing designs.

Hi designers, We wanted to share our thoughts on the main image of the flyer. We're leaning towards an image that shows a sole student on a computer with the computer screen in view. The computer screen could have the sample image we provided to show how the video classes operate. Thanks! The Trust of Reading Development

Graphic Design

```html
<!DOCTYPE html>
<html lang="en">
<head>
<meta charset="utf-8">
<title>Reading Skills Classes – Online this Summer</title>
<link rel="stylesheet" href="https://fonts.googleapis.com/css2?family=Lato:wght@400;700&family=PT+Sans:ital,wght@0,400;0,700;1,700&display=swap">
<style>
  :root {
    --cyan: #1db3d8;
    --charcoal: #262626;
    --white: #ffffff;
    --ink: #333333;
    --body: #6a6a6a;
    --rule: #5a5a5a;
    --photo-a: #c9cfb4;
    --photo-b: #8e9a6c;
    --photo-c: #e9e4d8;
  }
  * { margin: 0; padding: 0; box-sizing: border-box; }
  html, body { width: 927px; height: 1200px; overflow: hidden; background: var(--white); }
  .flyer { position: relative; width: 927px; height: 1200px; overflow: hidden; background: var(--white); font-family: "PT Sans", sans-serif; }

  .title-panel { position: absolute; left: 0; top: 0; width: 330px; height: 398px; background: var(--cyan); color: var(--white); font-family: "Lato", sans-serif; }
  .title-panel .word { position: absolute; left: 24px; font-weight: 700; line-height: 1; }
  .title-panel .w1 { top: 56px; font-size: 69px; }
  .title-panel .w2 { top: 136px; font-size: 69px; }
  .title-panel .w3 { top: 218px; font-size: 54px; }
  .title-panel .tagline { position: absolute; left: 24px; top: 296px; font-size: 29px; font-weight: 400; }

  .hero-photo { position: absolute; left: 330px; top: 0; width: 597px; height: 398px;
    background: linear-gradient(135deg, var(--photo-c) 0%, var(--photo-a) 45%, var(--photo-b) 100%); }

  .sidebar { position: absolute; left: 0; top: 398px; width: 330px; height: 802px; background: var(--charcoal); color: var(--white); }

  .features { position: absolute; left: 18px; top: 56px; list-style: none; }
  .feature { position: absolute; left: 0; display: flex; align-items: flex-start; width: 312px; font-size: 17px; line-height: 22px; white-space: nowrap; }
  .feature svg { flex: none; width: 32px; height: 32px; margin-right: 14px; margin-top: -5px; }
  .feature.f1 { top: 0; }
  .feature.f2 { top: 56px; }
  .feature.f3 { top: 111px; }
  .feature.f4 { top: 171px; }

  .skills { position: absolute; left: 36px; top: 330px; list-style: none; }
  .skill { position: relative; padding-left: 32px; height: 32px; font-size: 17px; font-weight: 700; line-height: 22px; }
  .skill::before { content: ""; position: absolute; left: 0; top: 7px; width: 9px; height: 9px; border-radius: 50%; background: var(--cyan); }

  .divider { position: absolute; left: 14px; top: 552px; width: 292px; height: 1px; background: var(--rule); }

  .contact { position: absolute; left: 24px; top: 566px; }
  .contact .heading { font-size: 27px; font-weight: 700; line-height: 37px; }
  .contact .phone { font-size: 22px; font-weight: 700; font-style: italic; margin-top: 4px; }
  .hours { margin-top: 24px; list-style: none; }
  .hours li { font-size: 20px; line-height: 32px; }
  .hours b { font-weight: 700; }

  .programs { position: absolute; left: 354px; top: 0; width: 560px; }
  .program { position: absolute; left: 0; width: 560px; }
  .program h3 { font-size: 16.5px; font-weight: 700; color: var(--ink); line-height: 20px; margin-bottom: 2px; }
  .program p { font-size: 14px; color: var(--body); line-height: 18px; }
  .p1 { top: 422px; } .p2 { top: 509px; } .p3 { top: 594px; } .p4 { top: 680px; }
  .p5 { top: 773px; } .p6 { top: 866px; } .p7 { top: 966px; }

  .partner-name { position: absolute; right: 16px; top: 1132px; display: flex; align-items: center; color: var(--charcoal); font-size: 22px; font-weight: 700; line-height: 28px; }
  .partner-name::before { content: ""; width: 14px; height: 14px; margin-right: 10px; background: var(--charcoal); }
</style>
</head>
<body>
<main class="flyer">
  <header class="title-panel">
    <span class="word w1">Reading</span>
    <span class="word w2">Skills</span>
    <span class="word w3">Classes</span>
    <span class="tagline">Online this Summer!</span>
  </header>

  <div class="hero-photo" role="img" aria-label="Photo of a child wearing headphones at a laptop, joining a live video class with a teacher on screen"></div>

  <aside class="sidebar">
    <ul class="features">
      <li class="feature f1">
        <svg viewBox="0 0 34 34" aria-hidden="true"><circle cx="17" cy="17" r="17" fill="#1db3d8"/><rect x="9" y="10" width="16" height="11" rx="1.5" fill="none" stroke="#fff" stroke-width="2"/><rect x="13" y="23" width="8" height="2" fill="#fff"/></svg>
        <span>Small class size</span>
      </li>
      <li class="feature f2">
        <svg viewBox="0 0 34 34" aria-hidden="true"><circle cx="17" cy="17" r="17" fill="#1db3d8"/><rect x="9" y="8" width="16" height="7" fill="#fff"/><circle cx="17" cy="18.5" r="2.6" fill="#fff"/><path d="M11.5 27c0-4 2.5-5.5 5.5-5.5s5.5 1.5 5.5 5.5z" fill="#fff"/></svg>
        <span>A skilled and encouraging teacher</span>
      </li>
      <li class="feature f3">
        <svg viewBox="0 0 34 34" aria-hidden="true"><circle cx="17" cy="17" r="17" fill="#1db3d8"/><circle cx="17" cy="13" r="4.5" fill="#fff"/><path d="M9 26c0-5 3.5-7.5 8-7.5s8 2.5 8 7.5z" fill="#fff"/></svg>
        <span>Individualized skills intruction</span>
      </li>
      <li class="feature f4">
        <svg viewBox="0 0 34 34" aria-hidden="true"><circle cx="17" cy="17" r="17" fill="#1db3d8"/><path d="M11 9h11a2 2 0 0 1 2 2v15H13a2 2 0 0 1-2-2z" fill="#fff"/><path d="M11 24a2 2 0 0 0 2 2" fill="none" stroke="#1db3d8" stroke-width="1.5"/></svg>
        <span>A program of independent<br>reading in great books</span>
      </li>
    </ul>

    <ul class="skills">
      <li class="skill">Phonics</li>
      <li class="skill">Comprehension</li>
      <li class="skill">Fluency</li>
      <li class="skill">Study Skills</li>
      <li class="skill">Speed Reading</li>
      <li class="skill">Love of Reading</li>
    </ul>

    <div class="divider"></div>

    <section class="contact">
      <p class="heading">For More Information<br>or to Register</p>
      <p class="phone">Call 1-800-555-0142</p>
      <ul class="hours">
        <li><b>Mon - Fri :</b> 5am - 7pm</li>
        <li><b>Sat :</b> 5am - 4pm</li>
        <li><b>Sun :</b> 6am- 4pm</li>
      </ul>
    </section>
  </aside>

  <section class="programs">
    <article class="program p1">
      <h3>Program for Preschoolers:</h3>
      <p>Students in this program build strong reading readiness skills.<br>Your child will learn letter recognition and beginning phonics, and develop the<br>motivation and love of reading that make learning to read easy, enjoyable, and successful.</p>
    </article>
    <article class="program p2">
      <h3>Program for Entering Kindergartners:</h3>
      <p>Students in this program learn beginning reading skills and develop a love of books.<br>Your child will learn letter recognition, phonics, and sight words, and will learn to sound<br>out short words.</p>
    </article>
    <article class="program p3">
      <h3>Program for Entering 1st Graders:</h3>
      <p>Students in this program learn to read independently. Your child will learn phonics and<br>sight words, build comprehension, and gain the skills and confidence needed for success<br>in first grade.</p>
    </article>
    <article class="program p4">
      <h3>Program for Entering 2nd Graders:</h3>
      <p>Students in this program become fluent, independent readers. Your child will make<br>significant gains in phonics and word-attack skills, fluency, and comprehension, and will<br>develop confidence and a love of reading.</p>
    </article>
    <article class="program p5">
      <h3>Program for Entering 3rd Graders:</h3>
      <p>Students in this program become strong independent readers. Your child will develop the<br>comprehension, fluency, and long-word decoding skills needed to read longer books with<br>ease, and will build confidence and a love of reading.</p>
    </article>
    <article class="program p6">
      <h3>Program for Entering 4th and 5th Graders:</h3>
      <p>Students in this program make substantial gains in comprehension, long-word decoding<br>skills, fluency, and reading speed. Your child will complete homework more quickly and<br>easily, be more successful in school, and become a strong, enthusiastic reader.</p>
    </article>
    <article class="program p7">
      <h3>Programs for Entering 6th-8th Graders and Entering 9th and 10th Graders:</h3>
      <p>Students in these programs make substantial gains in comprehension while doubling<br>reading speed. They also learn the best way to read textbooks, take notes, and study for<br>tests. As a result, students complete homework more quickly and easily, get better grades,<br>and enjoy reading more.</p>
    </article>
  </section>

  <p class="partner-name">Northfield University</p>
</main>
</body>
</html>
```